Corporate Branding - Web and Print

A UK based company will like to use an existing logo to create branding materials for all marketing related documents, including business card, prints, letterhead, Website, Twitter, Facebook, Instagram logo etc. This company serves high-end clientele in the fashion, health and wellness and as such high quality and class is of utmost importance.
Where the logo can be modernised without losing its character then experiment. The main thing is to have a corporate branding which can be used later for brochures, Business Plan infographics.
The prominent colour within the organisation is burnt orange with no secondary colour. However if you believe a secondary colour is needed then use it, otherwise keep it simple and classy. Any chosen colours have to match perfectly.
Target Market(s)
High net worth individuals
Industry/Entity Type
Health And Wellness
Contact Information for Business Card
classy
Look and feel
Each slider illustrates characteristics of the customer's brand and the style your logo design should communicate.

```html
<!DOCTYPE html>
<html lang="en">
<head>
<meta charset="utf-8">
<title>Aurelle Business Card</title>
<link href="https://fonts.googleapis.com/css2?family=Open+Sans:wght@400;600;700&display=swap" rel="stylesheet">
<style>
  :root {
    --burnt-orange: #f7941d;
    --card-frost: #f6f4f2;
    --page-bg: #e4e1de;
    --ink-white: #ffffff;
    --faint-mark: rgba(247, 148, 29, 0.28);
  }
  * { margin: 0; padding: 0; box-sizing: border-box; }
  html, body { width: 1200px; height: 900px; overflow: hidden; }
  body {
    position: relative;
    background: var(--page-bg);
    font-family: "Open Sans", Arial, sans-serif;
    color: var(--ink-white);
  }
  .card {
    position: absolute;
    overflow: hidden;
    box-shadow: 0 4px 14px rgba(0,0,0,0.12);
  }
  .card--front { left: 238px; top: 62px; width: 555px; height: 343px; }
  .card--back { left: 457px; top: 518px; width: 560px; height: 342px; }
  .card__frost {
    position: absolute; left: 0; top: 0; width: 100%;
    background: linear-gradient(180deg, #fbfaf9 0%, var(--card-frost) 100%);
  }
  .card--front .card__frost { height: 185px; }
  .card--back .card__frost { height: 187px; }
  .card__band {
    position: absolute; left: 0; bottom: 0; width: 100%;
    background: var(--burnt-orange);
  }
  .card--front .card__band { height: 158px; }
  .card--back .card__band { height: 155px; }

  .brand-dot {
    position: absolute; left: 229px; top: 18px;
    width: 90px; height: 90px; border-radius: 50%;
    background: var(--burnt-orange);
  }
  .brand-name {
    position: absolute; left: 0; width: 100%; top: 108px;
    text-align: center;
    font-weight: 700; font-size: 50px; letter-spacing: 4px;
    color: var(--burnt-orange); line-height: 1;
  }
  .brand-name--faint {
    top: 122px; font-size: 46px; color: var(--faint-mark);
  }

  .holder {
    position: absolute; right: 288px; top: 224px; text-align: right;
  }
  .holder__name { font-weight: 700; font-size: 19px; line-height: 24px; }
  .holder__role { font-size: 14.5px; line-height: 20px; }
  .holder__address { font-size: 14.5px; line-height: 17px; margin-top: 10px; }

  .contacts {
    position: absolute; left: 303px; top: 222px; list-style: none;
  }
  .contacts li {
    display: flex; align-items: center;
    font-size: 14.5px; height: 23px;
  }
  .contacts svg { width: 11px; height: 11px; margin-right: 11px; fill: var(--ink-white); }

  .social {
    position: absolute; left: 0; width: 100%; top: 266px;
    display: flex; justify-content: center; align-items: center;
  }
  .social__label { font-weight: 700; font-size: 18px; margin-right: 16px; }
  .social__dot {
    width: 30px; height: 30px; border-radius: 50%;
    background: var(--ink-white); margin: 0 12px;
  }
</style>
</head>
<body>
  <section class="card card--front">
    <div class="card__frost"></div>
    <div class="brand-dot"></div>
    <div class="brand-name">AURELLE</div>
    <div class="card__band"></div>
    <div class="holder">
      <div class="holder__name">Daniel Hartley</div>
      <div class="holder__role">Managing Director</div>
      <div class="holder__address">18 Linden Mews, Chelsea<br>London, SW3 4QT</div>
    </div>
    <ul class="contacts">
      <li><svg viewBox="0 0 24 24"><path d="M6.6 10.8a15 15 0 0 0 6.6 6.6l2.2-2.2c.3-.3.7-.4 1-.2 1.1.4 2.3.6 3.6.6.6 0 1 .4 1 1V20c0 .6-.4 1-1 1A17 17 0 0 1 3 4c0-.6.4-1 1-1h3.5c.6 0 1 .4 1 1 0 1.2.2 2.4.6 3.6.1.3 0 .7-.2 1z"/></svg>(020)-318-5547</li>
      <li><svg viewBox="0 0 24 24"><path d="M7 1h10a2 2 0 0 1 2 2v18a2 2 0 0 1-2 2H7a2 2 0 0 1-2-2V3a2 2 0 0 1 2-2zm0 3v14h10V4zm5 15.5a1 1 0 1 0 0 2 1 1 0 0 0 0-2z"/></svg>078-214-9630</li>
      <li><svg viewBox="0 0 24 24"><path d="M2 5h20v14H2zm2 2v.5l8 5 8-5V7l-8 5z"/></svg>hello@aurelle.co.uk</li>
      <li><svg viewBox="0 0 24 24"><path d="M12 2a10 10 0 1 0 0 20 10 10 0 0 0 0-20zm-1 17.9A8 8 0 0 1 4.2 10L9 15v1a2 2 0 0 0 2 2zm6.9-2.5A2 2 0 0 0 16 16h-1v-3a1 1 0 0 0-1-1H8v-2h2a1 1 0 0 0 1-1V7h2a2 2 0 0 0 2-2v-.4a8 8 0 0 1 2.9 12.8z"/></svg>www.aurelle.co.uk</li>
    </ul>
  </section>

  <section class="card card--back">
    <div class="card__frost"></div>
    <div class="brand-name brand-name--faint">AURELLE</div>
    <div class="card__band">
      <div class="social" style="top:76px;">
        <span class="social__label">Follow us on</span>
        <span class="social__dot" aria-label="Social profile"></span>
        <span class="social__dot" aria-label="Social profile"></span>
        <span class="social__dot" aria-label="Social profile"></span>
      </div>
    </div>
  </section>
</body>
</html>
```